UPDATE: I have uploaded the selected logo from the other contest, please use it in your designs.

I have a logo design contest as well so not sure how PixelGuild handles that. They should integrate at some point. I will describe the overall theme with the logo description. See it for details.

The business card side of it would just build on that same theme.

Target Market(s)

8-40

Industry/Entity Type

Business

Contact Information for Business Card

FirstName LastName
Email

Logo Text

Velimor

Font styles to use
Sans Serif

Requirements
Must have
• the url Velimor.com somewhere in it.

```html
<!DOCTYPE html>
<html lang="en">
<head>
<meta charset="utf-8">
<title>Velimor Business Card</title>
<link rel="stylesheet" href="https://fonts.googleapis.com/css2?family=Michroma&family=Open+Sans:wght@400;600&display=swap">
<style>
  :root {
    --backdrop: #ececee;
    --card: #ffffff;
    --brand-green: #8dc63f;
    --brand-blue: #1a75bc;
    --accent-purple: #5b2a86;
    --ink: #222222;
    --ink-soft: #555555;
    --icon: #6b6b6b;
  }
  * { margin: 0; padding: 0; box-sizing: border-box; }
  html, body { width: 1200px; height: 600px; overflow: hidden; }
  body {
    background: var(--backdrop);
    font-family: "Open Sans", sans-serif;
    position: relative;
  }
  .card {
    position: absolute;
    top: 152px;
    width: 467px;
    height: 278px;
    background: var(--card);
    border-radius: 18px;
    overflow: hidden;
    box-shadow: 0 2px 6px rgba(0,0,0,0.08);
  }
  .card--front { left: 93px; }
  .card--back { left: 638px; }
  .card__band {
    position: absolute;
    left: 0; bottom: 0;
    width: 467px; height: 26px;
  }
  .wordmark {
    position: absolute;
    font-family: "Michroma", sans-serif;
    color: var(--brand-blue);
    letter-spacing: 0.12em;
    text-transform: uppercase;
    white-space: nowrap;
  }
  .card--front .wordmark {
    left: 0; right: 0;
    top: 112px;
    text-align: center;
    font-size: 36px;
    line-height: 44px;
  }
  .card--back .wordmark {
    left: 22px;
    top: 118px;
    font-size: 19px;
    line-height: 24px;
  }
  .contact {
    position: absolute;
    left: 233px;
    top: 62px;
    height: 130px;
    border-left: 1.5px solid var(--accent-purple);
    padding-left: 9px;
  }
  .contact__name {
    font-size: 16px;
    font-weight: 400;
    color: var(--ink);
    line-height: 20px;
    margin-top: 14px;
  }
  .contact__role {
    font-size: 11.5px;
    color: var(--ink-soft);
    line-height: 15px;
  }
  .contact__line {
    display: flex;
    align-items: center;
    gap: 5px;
    font-size: 11px;
    color: var(--ink-soft);
    line-height: 14px;
  }
  .contact__line--email { margin-top: 18px; }
  .contact__line--web { margin-top: 20px; }
  .contact__line b { font-weight: 600; color: var(--ink); }
  .contact__line--web b { color: var(--brand-blue); }
  .contact__icon { width: 10px; height: 10px; flex: none; }
</style>
</head>
<body>

  <section class="card card--front" aria-label="Business card front">
    <div class="wordmark">Velimor</div>
    <svg class="card__band" viewBox="0 0 467 26" aria-hidden="true">
      <rect x="0" y="0" width="467" height="2" fill="var(--accent-purple)"/>
      <polygon points="0,2 231,2 216,26 0,26" fill="var(--brand-green)"/>
      <polygon points="234,2 467,2 467,26 219,26" fill="var(--brand-blue)"/>
    </svg>
  </section>

  <section class="card card--back" aria-label="Business card back">
    <div class="wordmark">Velimor</div>
    <div class="contact">
      <p class="contact__name">Dana Whitfield</p>
      <p class="contact__role">Creative Manager</p>
      <p class="contact__line contact__line--email">
        <svg class="contact__icon" viewBox="0 0 10 10" aria-hidden="true">
          <rect x="0.5" y="2" width="9" height="6.5" fill="var(--icon)"/>
          <polyline points="0.5,2 5,5.8 9.5,2" fill="none" stroke="#fff" stroke-width="0.9"/>
        </svg>
        <span>danawhitfield@<b>velimor</b>.com</span>
      </p>
      <p class="contact__line contact__line--web">
        <svg class="contact__icon" viewBox="0 0 10 10" aria-hidden="true">
          <circle cx="5" cy="5" r="4.5" fill="var(--icon)"/>
          <ellipse cx="5" cy="5" rx="2" ry="4.5" fill="none" stroke="#fff" stroke-width="0.7"/>
          <line x1="0.5" y1="5" x2="9.5" y2="5" stroke="#fff" stroke-width="0.7"/>
        </svg>
        <span>www.<b>Velimor</b>.com</span>
      </p>
    </div>
    <svg class="card__band" viewBox="0 0 467 26" aria-hidden="true">
      <rect x="0" y="0" width="467" height="2" fill="var(--accent-purple)"/>
      <polygon points="0,2 231,2 216,26 0,26" fill="var(--brand-green)"/>
      <polygon points="234,2 467,2 467,26 219,26" fill="var(--brand-blue)"/>
    </svg>
  </section>

</body>
</html>
```